FlockVault.net website design

We are looking for a design for a new website we are about to launch called FlockVault.net. FlockVault.net is an online discount wine site that will focus on selling only one wine at a time. (This potentially may become two or three wines at a time in the future but only one for now). The wine that is up for sale will not actually be sold until a pre-set number of buyers “the group” commits to buying the wine. If the threshold of buyers is not met then the wine is not sold. This group aspect is what makes the site unique. By only selling the wine when the group commits to buying it we are able to deliver them a great wine at a fantastic price.
The website should convey a fun feeling while also indicating that this is a place where serious wine enthusiasts can shop. We will be providing information, ratings, and reviews about the wines that are currently on sale.
Updates
Target Market(s)
The target market is a wide range of wine enthusiasts, from people in their 20s and 30s to more mature and serious wine connoisseurs.
Industry/Entity Type
Shop
Requirements
Must have
- Below is a list of specifications for the website:
1) Main page with our logo (which includes green, purple, and a magenta wine color) that showcases the current wine that's for sale
- The site’s main focus should be on selling ONE bottle of wine at a time at group rate.
- The site should capture the group buying concept as this is what differentiates our site from the others. Visitors to the site should get the sense that they are part of a special community that is getting a great deal because they are buying the wine as a group.
- A meter or better yet an animation should be used to indicate if the tipping point has been met for a sale. We’d like to see some creative ideas here.
- Nice high-res photo of the wine bottle
- Detailed description of what kind of wine it is, where the wine is from, type of grape, vino observer and other ratings, description of what it tastes like. We would like the option to provide as much detail here as possible.
- Breakdown on what the prices are per bottle and the discount we're giving. We would like to show the original price as compared to the FlockVault.net price.
- Potentially show a list of upcoming wines. Maybe not the exact wine that will be for sale next but some info to entice users to keep checking.
2) User Account Log in
- Ability to create and log into a personal account
The personal account should be able to:
-store users' credit card and shipping information as well as past orders
-allow you to opt in or out of flock vault emails
-potentially store wine preference or ratings information
-refer a friend option where you get some kind of incentive
3) The Group Concept. The website design must include a few aspects that identify FlockVault.net as a social site, not simply a wine sale site.
- Some kind of indicator showing if the group threshold has been met or not. We would like to see some type of animation with wine bottles filling up, or grapes on a scale-something that would change as the number of people buying into the sale increase.
- Button to join the group purchase
4) General Site Content must include:
- Email link to send questions to support
- Information on how shipping works and other FAQs
- Legal disclaimer
- Links to Friendbook and Chirper
Nice to have
- It would be nice to have a discussion board where FlockVault members can discuss wines.
Should not have
- The design should not be for a general wine store that sells a variety of different wines.

```html
<!DOCTYPE html>
<html lang="en">
<head>
<meta charset="utf-8">
<title>FlockVault.net – One bottle at group rate</title>
<link rel="stylesheet" href="https://fonts.googleapis.com/css2?family=Great+Vibes&family=Open+Sans:wght@400;600;700&family=Questrial&display=swap">
<style>
:root{
  --leaf:#8dbb2e;
  --leaf-dark:#5f9320;
  --leaf-light:#a8cf45;
  --plum:#8e3f97;
  --magenta:#b3326f;
  --rose:#c04c7f;
  --blush:#f3dde6;
  --blush-line:#e4c3d1;
  --ink:#444;
  --soft:#fafaf7;
  --rule:#cfcfcf;
  --ember:#c84a12;
  --ember-light:#e2741c;
}
*{box-sizing:border-box;margin:0;padding:0}
html,body{width:1200px;height:1071px;overflow:hidden;background:var(--soft)}
body{font-family:"Open Sans",Arial,sans-serif;color:var(--ink);font-size:10.5px}
.page{position:relative;width:1200px;height:1071px;overflow:hidden;background:var(--soft)}
.abs{position:absolute}
.header-bg{left:0;top:0;width:1200px;height:138px;background:linear-gradient(180deg,#8cbb35 0,#9cc744 70%,#c9e08e 92%,var(--soft) 100%)}
.brand{left:152px;top:150px;width:320px;height:75px}
.brand-dot{left:2px;top:8px;width:52px;height:52px;border-radius:50%;background:var(--plum)}
.brand-name{left:76px;top:18px;font-family:"Questrial",sans-serif;font-size:38px;color:var(--leaf);letter-spacing:-.5px;line-height:1;white-space:nowrap}
.brand-tag{left:84px;top:62px;font-size:9.5px;font-style:italic;font-weight:600;color:var(--plum);white-space:nowrap}
.nav{left:541px;top:186px;display:flex;gap:3px}
.nav a{display:block;height:34px;line-height:34px;padding:0 14px;font-weight:700;font-size:13px;color:var(--magenta);text-decoration:none;background:linear-gradient(#fdfdfb,#eeeeea);border:1px solid #dcdcd6;border-radius:3px}
.nav a.current{background:var(--plum);color:#fff;border-color:var(--plum)}
.rule{height:5px;background:repeating-linear-gradient(135deg,var(--rule) 0 1px,transparent 1px 3px)}
.top-rule{left:152px;top:237px;width:895px}
.hero{left:152px;top:257px;width:662px;height:207px;border-radius:4px;overflow:hidden;background:linear-gradient(90deg,#6e2612 0,#4a150f 55%,#2a0a0c)}
.hero-photo{left:420px;top:0;width:242px;height:207px;background:linear-gradient(90deg,rgba(90,12,20,0),#6a1018 40%,#3a0a10)}
.hero-line{font-family:"Great Vibes",cursive;color:#fff;font-size:46px;line-height:1;white-space:nowrap}
.hero-line.one{left:38px;top:52px}
.hero-line.two{left:34px;top:104px;font-size:42px}
.hero-line .accent{color:var(--leaf-light);font-size:48px}
.product{left:152px;top:478px;width:662px;height:320px;background:#fff;border:1px solid #ddd;border-radius:4px}
.product-bottle{left:40px;top:28px;width:64px;height:212px;border-radius:3px;background:linear-gradient(90deg,#2a1a1e,#4a2430 50%,#2a1a1e)}
.details{left:133px;top:10px;width:518px;height:255px;border:1px solid #ddd;background:#fcfcfc}
.details .inner{position:absolute;left:16px;top:12px;width:488px}
.label{color:var(--magenta);font-weight:700;font-size:10.5px}
.desc p{font-size:9.8px;line-height:15px;margin-top:2px}
.fact{border-top:1px dotted #ccc;padding:8px 0 9px;font-size:9.8px;white-space:nowrap}
.fact .label{margin-right:5px}
.desc{padding-bottom:7px}
.more{position:absolute;left:0;bottom:0;width:100%;height:22px;line-height:22px;text-align:center;background:#ececec;font-weight:700;font-size:10px;color:#222}
.more svg{vertical-align:middle;margin-left:3px}
.prices{left:133px;top:281px;width:518px;font-weight:700;white-space:nowrap}
.price{font-size:17px;color:var(--leaf)}
.price b{color:#444}
.price+.price{margin-left:14px}
.discount{position:absolute;right:0;top:-4px;font-size:23px;color:var(--magenta)}
.discount b{color:#444;font-weight:600}
.upcoming{left:152px;top:811px;width:662px;height:76px;border-radius:4px;overflow:hidden;background:linear-gradient(90deg,#b53a0c,var(--ember-light) 70%,var(--ember))}
.upcoming-photo{left:0;top:0;width:242px;height:76px;background:linear-gradient(90deg,#6a5026,#5a3a20 60%,#b53a0c)}
.upcoming h2{position:absolute;left:243px;top:10px;font-size:14px;color:#d9f08a;font-weight:700}
.upcoming ul{position:absolute;left:243px;top:33px;list-style:none;color:#fff;font-size:9.8px;line-height:17px}
.upcoming li:before{content:"•";margin-right:5px}
.pager{right:10px;bottom:8px;display:flex;gap:3px}
.pager span{width:12px;height:10px;background:#5a2510;border-radius:2px}
.login{left:831px;top:257px;width:216px;height:321px;background:#fff6f8;border:1px solid #e8d5dc;border-radius:4px}
.ribbon{left:-11px;top:11px;width:239px;height:46px}
.ribbon-title{left:40px;top:21px;color:#fff;font-weight:700;font-size:14.5px}
.field{position:absolute;left:10px;width:197px;height:28px;background:var(--blush);border:1px solid var(--blush-line);border-radius:3px;padding:7px 10px;font-size:9.5px}
.field.tall{height:38px}
.opts{left:15px;top:163px;font-size:9.5px;display:flex;gap:20px}
.opts span:before{content:"";display:inline-block;width:11px;height:11px;border:1px solid #3b4f80;margin-right:5px;vertical-align:-2px;background:#fff}
.links{left:10px;top:279px;font-size:9.5px;line-height:15px}
.links div:before{content:"›";margin-right:4px;color:#888}
.login-btn{left:114px;top:277px;width:92px;height:32px;border-radius:3px;background:linear-gradient(#b15aba,var(--plum));color:#fff;font-weight:700;font-size:15px;text-align:center;line-height:32px}
.meter{left:855px;top:598px;width:42px;height:170px;border-radius:4px;background:var(--leaf);overflow:hidden}
.meter-fill{left:0;bottom:0;width:42px;height:102px;background:var(--plum)}
.meter-label{left:0;top:96px;width:42px;text-align:center;color:#fff;font-weight:700;font-size:11px}
.meter-text{left:914px;top:593px;font-weight:700;color:var(--rose);font-size:26px;line-height:26px}
.meter-text .sale{color:var(--plum);font-size:36px;line-height:38px;border-top:1px solid #ccc;border-bottom:1px solid #ccc;display:inline-block}
.meter-text .inc{color:#555;font-size:23px;line-height:28px;display:block}
.join{left:913px;top:741px;width:102px;height:28px;border-radius:3px;background:linear-gradient(#a9d64a,#6ea523);color:#fff;font-weight:700;font-size:16px;text-align:center;line-height:28px}
.side-rule{left:831px;top:790px;width:216px}
.social{left:845px;top:818px;font-size:11px;font-weight:700;color:#333;line-height:13px}
.social .row{display:flex;align-items:center;gap:12px;height:37px}
.social i{width:20px;height:22px;background:var(--plum);display:block}
.social em{font-style:normal;color:var(--leaf-dark);display:block}
.glasses-photo{left:950px;top:814px;width:85px;height:76px;border-radius:3px;background:linear-gradient(180deg,#e8d89a,#b8303e)}
.footer-bg{left:0;top:958px;width:1200px;height:113px;background:linear-gradient(180deg,var(--soft) 0,#a6c868 12%,#6a9e24 30%,#62961e 100%)}
.footer-links{left:152px;top:1009px;color:#fff;font-size:10px}
.footer-links a{color:#fff;text-decoration:none}
.footer-links a.current{color:#dff59a}
.footer-links .sep{margin:0 5px}
.copy{left:153px;top:1026px;color:#fff;font-size:10px}
.foot-brand{left:816px;top:998px}
.foot-brand .dot{position:absolute;left:0;top:2px;width:40px;height:40px;border-radius:50%;background:#4d7a1b}
.foot-brand .name{position:absolute;left:56px;top:6px;font-family:"Questrial",sans-serif;font-size:29px;color:#3f6a14;white-space:nowrap}
.foot-brand .tag{position:absolute;left:62px;top:42px;font-size:8px;font-style:italic;color:#3f6a14;white-space:nowrap}
</style>
</head>
<body>
<div class="page">

  <div class="abs header-bg" role="img" aria-label="Vine banner with green grapes, red grapes and a white wine bottle"></div>

  <header>
    <div class="abs brand">
      <span class="abs brand-dot"></span>
      <span class="abs brand-name">FlockVault</span>
      <span class="abs brand-tag">The lowest prices are down in the vault</span>
    </div>
    <nav class="abs nav">
      <a class="current" href="#">HOME</a>
      <a href="#">SUPPORT</a>
      <a href="#">DISCLAIMER</a>
      <a href="#">INFO ON SHIPPING</a>
      <a href="#">FAQS</a>
    </nav>
  </header>
  <div class="abs rule top-rule"></div>

  <section class="abs hero">
    <div class="abs hero-photo" role="img" aria-label="Glass of red wine with a bottle, grapes and a pomegranate"></div>
    <div class="abs hero-line one">One Bottle of Wine</div>
    <div class="abs hero-line two">at a time at <span class="accent">Group Rate</span></div>
  </section>

  <section class="abs product">
    <div class="abs product-bottle" role="img" aria-label="Bottle of red wine"></div>
    <div class="abs details">
      <div class="inner">
        <div class="desc">
          <div class="label">Detailed Description :</div>
          <p>There are many variations of passages of Lorem Ipsum available, but the majority have suffered alteration in some form, by injected humour, or randomised words which don't look even slightly believable. If you are going to use a passage of Lorem Ipsum, you need to be sure there isn't anything embarrassing hidden in the middle of text.</p>
        </div>
        <div class="fact"><span class="label">Where the wine is from :</span> There are many variations of passages of Lorem Ipsum available.</div>
        <div class="fact"><span class="label">Type of Grape :</span> There are many variations of passages of Lorem Ipsum available.</div>
        <div class="fact"><span class="label">Vino observer &amp; Ratings :</span> There are many variations of passages of Lorem Ipsum available.</div>
        <div class="fact"><span class="label">Taste of wine :</span> There are many variations of passages of Lorem Ipsum available.</div>
      </div>
      <div class="more">Show more details<svg width="9" height="8" viewBox="0 0 9 8"><path d="M1 1l3.5 3 3.5-3M1 4l3.5 3 3.5-3" fill="none" stroke="#8dbb2e" stroke-width="1.3"/></svg></div>
    </div>
    <div class="abs prices">
      <span class="price">List Price : <b>$50</b></span>
      <span class="price">Our Price : <b>$40</b></span>
      <span class="discount">Discount : <b>20%</b></span>
    </div>
  </section>

  <section class="abs upcoming">
    <div class="abs upcoming-photo" role="img" aria-label="Grapes, a wooden barrel and a candle by a cellar window"></div>
    <h2>Upcoming Wines</h2>
    <ul>
      <li>Contrary to popular belief, Lorem Ipsum is not simply random text. It has roots in a piece.</li>
      <li>Classical Latin literature from 45 BC.</li>
    </ul>
    <div class="abs pager"><span></span><span></span></div>
  </section>

  <aside>
    <div class="abs login">
      <svg class="abs ribbon" viewBox="0 0 239 46" aria-hidden="true">
        <path d="M0 0H239V38H218L6 38L12 19Z" fill="#b73f77"/>
        <path d="M228 38H239L228 46Z" fill="#7a1f4e"/>
      </svg>
      <div class="abs ribbon-title">USER LOG IN</div>
      <div class="field" style="top:61px">User Name :</div>
      <div class="field" style="top:96px">Password :</div>
      <div class="field" style="top:131px">Flock vault emails :</div>
      <div class="abs opts"><span>opt in</span><span>opt out</span></div>
      <div class="field tall" style="top:184px">Shipping Information :</div>
      <div class="field tall" style="top:229px">Ratings Information :</div>
      <div class="abs links"><div>Refer a friend</div><div>Create an account</div></div>
      <div class="abs login-btn">LOG IN</div>
    </div>

    <div class="abs meter" role="img" aria-label="Group meter, 60 percent filled">
      <div class="abs meter-fill"></div>
      <div class="abs meter-label">60 %</div>
    </div>
    <div class="abs meter-text">People<br>Buying<br>into the<br><span class="sale">SALE</span><span class="inc">increase</span></div>
    <div class="abs join">JOIN</div>

    <div class="abs rule side-rule"></div>
    <div class="abs social">
      <div class="row"><i></i><span>Find us on<em>FRIENDBOOK</em></span></div>
      <div class="row"><i></i><span>follow us on<em>CHIRPER</em></span></div>
    </div>
    <div class="abs glasses-photo" role="img" aria-label="Two glasses of wine with grapes"></div>
  </aside>

  <div class="abs footer-bg" role="img" aria-label="Green vine footer band with grapes"></div>
  <footer>
    <div class="abs footer-links">
      <a class="current" href="#">Home</a><span class="sep">|</span><a href="#">Suppor</a><span class="sep">|</span><a href="#">Disclaimer</a><span class="sep">|</span><a href="#">Info on shipping</a><span class="sep">|</span><a href="#">FAQs</a>
    </div>
    <div class="abs copy">Copyright © 2011 FlockVault.net. All Rights Reserved.</div>
    <div class="abs foot-brand">
      <span class="dot"></span>
      <span class="name">FlockVault</span>
      <span class="tag">The lowest prices are down in the vault</span>
    </div>
  </footer>
</div>
</body>
</html>
```